Lumoran signs for fridge and desk

I require 3 a4 designs very basic designs with single colour and easy to print. I have atached a style guide to see the fonts I used in my last three design. Please remember I'm printing in only one colour
PLease see the following link, of what I sell on quorbit. I will be selling this allong side these products.
https://www.quorbitshop.example/gp/item/K42H9XRDLM
Please see my competitors
https://www.quorbitshop.example/Planner-Magnetic-Calendar-Refrigerator-Container/dp/K7TQR2ZMWA/ref=sr_1_8?keywords=acrylic%2Bnote%2Bboard%2Brefrigerator%2Bdry%2Berase%2Bboard%2Bmagnetic%2Bclear&qid=1500000001&sr=8-8&th=1
and
https://www.quorbitshop.example/Magnetic-Acrylic-Calendar-Fridge-Refrigerator/dp/K9PWX4HNVE/ref=sr_1_4_sspa?keywords=acrylic+note+board+refrigerator+dry+erase+board+magnetic+clear&qid=1500000002&sr=8-4-spons&psc=1&spLa=UXhMbTNwZkRzWXZLcTJ3Rm5CaFRnSmRWZUx5UG1Sb1phSXVPY0F0TmJXa0dmWnNZeEhqUXJUbkxwVmRNZ0ViS2N5SXdBb0J1RnpQbVhoU2pOdFlxUmdDa1d2RHNMZUZuSHBaeEJtQ2tUZ1lqVnJRc0Vh
I'd like something more fun and different. But that can still be printed on Lumoran with one colour and be functional. A shopping list, a weekly planner(both that stick to a fridge) and a to do list that will sit on a desk or kitchen counter top.
PLease design
1st a4
Break into seven parts, with seven headings..... Monday to Sunday.... here customers will be able to write menus and upcoming events. I want this landcape
2nd a4
'Shopping List' is to be the heading
I want this landcape
3rd a4
'To Do List' is the only text I would like
I would like this portrat and lines marked and a check box on the left hand side
Remember I can only print on the acrylic with one colour. I want to be different from my competitors but I do want to be functional.
just a reminder. I can only print with one colour

```html
<!DOCTYPE html>
<html lang="en">
<head>
<meta charset="utf-8">
<title>Lumoran Weekly Planner</title>
<link rel="stylesheet" href="https://fonts.googleapis.com/css2?family=Roboto+Condensed:wght@800;900&display=swap">
<style>
  :root {
    --ink: #000000;
    --paper: #ffffff;
  }
  html, body {
    margin: 0;
    padding: 0;
    width: 1200px;
    height: 849px;
    overflow: hidden;
    background: var(--paper);
  }
  .planner {
    display: block;
    width: 1200px;
    height: 849px;
  }
  .day-tab { fill: var(--ink); }
  .day-initial {
    font-family: "Roboto Condensed", "Arial Narrow", sans-serif;
    font-weight: 900;
    font-size: 76px;
  }
  .day-name {
    font-family: "Roboto Condensed", "Arial Narrow", sans-serif;
    font-weight: 800;
    font-size: 31px;
    text-anchor: middle;
  }
  .on-dark { fill: var(--paper); }
  .on-light { fill: var(--ink); }
  .rule, .divider, .note-box {
    fill: none;
    stroke: var(--ink);
    stroke-width: 1.6;
    stroke-dasharray: 16 3 1.6 3 1.6 3;
  }
</style>
</head>
<body>
<svg class="planner" viewBox="0 0 1200 849" xmlns="http://www.w3.org/2000/svg" aria-label="Weekly planner, Monday to Sunday">
  <defs>
    <clipPath id="header-clip">
      <rect x="0" y="26" width="1200" height="100"/>
    </clipPath>
  </defs>

  <!-- Header tabs -->
  <g class="header">
    <path class="day-tab" d="M26.7 122 V55 A29 29 0 0 1 55.7 26 H190.2 V122 Z"/>
    <rect class="day-tab" x="354.3" y="26" width="163.6" height="96"/>
    <rect class="day-tab" x="682" y="26" width="163.6" height="96"/>
    <path class="day-tab" d="M1009.7 122 V26 H1144.2 A29 29 0 0 1 1173.2 55 V122 Z"/>

    <g clip-path="url(#header-clip)">
      <text class="day-initial on-dark" x="190.2" y="80" text-anchor="end">M</text>
      <text class="day-initial on-light" x="354.3" y="80" text-anchor="end">T</text>
      <text class="day-initial on-dark" x="517.9" y="80" text-anchor="end">W</text>
      <text class="day-initial on-light" x="682" y="80" text-anchor="end">T</text>
      <text class="day-initial on-dark" x="845.6" y="80" text-anchor="end">F</text>
      <text class="day-initial on-light" x="1011" y="80" text-anchor="end">S</text>
      <text class="day-initial on-dark" x="1174" y="80" text-anchor="end">S</text>
    </g>

    <text class="day-name on-dark" x="108.5" y="102">MONDAY</text>
    <text class="day-name on-light" x="272.3" y="102">TUESDAY</text>
    <text class="day-name on-dark" x="436.1" y="102">WEDNESDAY</text>
    <text class="day-name on-light" x="600" y="102">THURSDAY</text>
    <text class="day-name on-dark" x="763.8" y="102">FRIDAY</text>
    <text class="day-name on-light" x="927.7" y="102">SATURDAY</text>
    <text class="day-name on-dark" x="1091.5" y="102">SUNDAY</text>
  </g>

  <!-- Writing grid -->
  <g class="grid">
    <line class="divider" x1="190.2" y1="137.4" x2="190.2" y2="734.3"/>
    <line class="divider" x1="354.3" y1="137.4" x2="354.3" y2="734.3"/>
    <line class="divider" x1="517.9" y1="137.4" x2="517.9" y2="734.3"/>
    <line class="divider" x1="682" y1="137.4" x2="682" y2="734.3"/>
    <line class="divider" x1="845.6" y1="137.4" x2="845.6" y2="734.3"/>
    <line class="divider" x1="1009.7" y1="137.4" x2="1009.7" y2="734.3"/>

    <line class="rule" x1="27.7" y1="183.4" x2="1172" y2="183.4"/>
    <line class="rule" x1="27.7" y1="229.9" x2="1172" y2="229.9"/>
    <line class="rule" x1="27.7" y1="276.4" x2="1172" y2="276.4"/>
    <line class="rule" x1="27.7" y1="322.9" x2="1172" y2="322.9"/>
    <line class="rule" x1="27.7" y1="369.4" x2="1172" y2="369.4"/>
    <line class="rule" x1="27.7" y1="415.9" x2="1172" y2="415.9"/>
    <line class="rule" x1="27.7" y1="462.4" x2="1172" y2="462.4"/>
    <line class="rule" x1="27.7" y1="508.9" x2="1172" y2="508.9"/>
    <line class="rule" x1="27.7" y1="555.4" x2="1172" y2="555.4"/>
    <line class="rule" x1="27.7" y1="601.9" x2="1172" y2="601.9"/>
    <line class="rule" x1="27.7" y1="648.4" x2="1172" y2="648.4"/>
    <line class="rule" x1="27.7" y1="694.9" x2="1172" y2="694.9"/>
  </g>

  <!-- Note boxes -->
  <g class="notes">
    <path class="note-box" d="M26.7 750 H190.2 V822 H50.7 A24 24 0 0 1 26.7 798 Z"/>
    <rect class="note-box" x="354.3" y="750" width="163.6" height="72"/>
    <rect class="note-box" x="682" y="750" width="163.6" height="72"/>
    <path class="note-box" d="M1009.7 750 H1173.2 V798 A24 24 0 0 1 1149.2 822 H1009.7 Z"/>
  </g>
</svg>
</body>
</html>
```